Guided Study Tour - Klangtage Dornhalm Two Sided Flyer

We need a two-sided flyer for a Guided Study Tour to Klangtage Dornhalm. We want beautiful pictures of Germany and if possible some of the Velter venues our participants will be visiting. I have also provided the content that needs to be included. Also, in the attached document I provided a link to the Klangtage event. Please read and watch the video to be inspired.
This flyer should be beautiful and engaging. It needs to grab your attention right away and really highlight the wonderful things that they will be doing and that are included in the tour. This is a once in a lifetime opportunity for people to experience. We are targeting Music Directors and Music professionals.
Both attached logos need to be present on the flyer.

```html
<!DOCTYPE html>
<html lang="en">
<head>
<meta charset="utf-8">
<title>Klangtage Dornhalm Guided Study Tour Flyer</title>
<link href="https://fonts.googleapis.com/css2?family=Noto+Serif&family=Playfair+Display:wght@900&family=PT+Sans:wght@400;700&family=Arvo&display=swap" rel="stylesheet">
<style>
:root{
  --stage:#0f1d2a;
  --sand:#c4b59a;
  --tan:#c39a6c;
  --ink:#1e1e1e;
  --white:#ffffff;
  --label:#55606b;
  --accent:#c08a4f;
  --logo-red:#b3232a;
  --logo-blue:#24408e;
}
*{margin:0;padding:0;box-sizing:border-box}
html,body{width:1200px;height:962px;overflow:hidden;background:var(--stage)}
.canvas{position:relative;width:1200px;height:962px;font-family:"PT Sans",sans-serif}
.panel{position:absolute;top:86px;width:525px;height:744px;overflow:hidden}
.panel--back{left:61px;background:var(--sand)}
.panel--front{left:607px;background:var(--white);height:742px}
.side-label{position:absolute;top:842px;font-family:"Arvo",serif;font-size:37px;color:var(--label);width:525px;text-align:center}
.side-label--back{left:61px}.side-label--front{left:607px}

/* back */
.block{position:absolute;left:45px;right:30px;color:var(--white)}
.heading{font-size:15px;font-weight:400;color:var(--ink);letter-spacing:.1px}
.bullets{list-style:none;font-size:8.4px}
.bullets li{position:relative;padding-left:12px}
.bullets li::before{content:"";position:absolute;left:2px;top:50%;margin-top:-4px;border-left:5px solid var(--ink);border-top:4px solid transparent;border-bottom:4px solid transparent}
.bullets li.cont::before{display:none}
.bullets--wide li{line-height:17.6px}
.bullets--study li{line-height:14.4px}
.bullets--trip li{line-height:16px}
.performers{font-size:8.4px;font-weight:700}
.para{font-size:8.4px;line-height:10.5px}
.contact{font-size:11px;font-weight:700;padding-left:12px}
.logo-band{position:absolute;left:0;top:665px;width:525px;height:57px;background:var(--white);display:flex;align-items:center;justify-content:space-around}
.logo-band__base{position:absolute;left:0;top:722px;width:525px;height:22px;background:var(--tan)}
.partner{display:flex;align-items:center;gap:7px;font-family:"PT Sans",sans-serif;font-weight:700;font-size:17px}
.partner--meridian{color:var(--logo-blue)}
.partner--garnet{color:var(--logo-red)}
.partner__mark{width:20px;height:20px;border-radius:50%;background:currentColor}

/* front */
.front-art{position:absolute;left:0;top:0}
.front-text{position:absolute;left:0;width:525px;text-align:center}
.date{top:40px;font-family:"Noto Serif",serif;font-size:26px;color:var(--ink)}
.tour{top:78px;font-family:"Playfair Display",serif;font-weight:900;font-size:38px;color:var(--white);font-variant:small-caps;letter-spacing:.5px;line-height:1}
.fest{top:116px;font-family:"Playfair Display",serif;font-weight:900;font-size:64px;color:var(--white);letter-spacing:1px;line-height:1}
.place{top:184px;font-family:"Noto Serif",serif;font-size:30px;color:var(--ink)}
.invite{top:236px;font-family:"Noto Serif",serif;font-size:21px;line-height:27px;color:var(--white)}
.quote{position:absolute;left:162px;top:492px;width:200px;text-align:center;color:var(--ink)}
.quote__title{font-family:"Noto Serif",serif;font-size:14px;color:var(--accent);margin-bottom:4px}
.quote__text{font-size:7.8px;line-height:10px}
.quote__name{font-size:12.5px;margin-top:6px}
.quote__role{font-size:8px;font-style:italic}
</style>
</head>
<body>
<div class="canvas">

  <section class="panel panel--back" aria-label="Back of flyer">
    <div class="block" style="top:30px">
      <h2 class="heading">Klangtage Highlights</h2>
      <ul class="bullets bullets--wide" style="margin-top:4px">
        <li>More than 100 Concerts in 42 different Velter venues</li>
        <li>World Class Musicians &amp; Celebrated Recording Artists</li>
        <li>Day trips to Weimar &amp; Dresden</li>
        <li>Bilingual pre-concert talks &amp; lectures with Velter Scholars</li>
      </ul>
    </div>

    <div class="block" style="top:137px">
      <h2 class="heading">Featured Performers</h2>
      <p class="performers" style="margin-top:3px">Jonas Varga, Tom Kessler, Armonia, Dornhalm Hall Orchestra, Silvana &amp; the Dornhalm Boys Choir</p>
    </div>

    <div class="block" style="top:177px">
      <h2 class="heading">Study Tour Highlights</h2>
      <ul class="bullets bullets--study" style="margin-top:3px">
        <li>Access to dress rehearsals</li>
        <li>Meet the artist opportunities</li>
        <li>Post-concert discussions led by Daniel Marsh</li>
        <li>Study sessions on Velter's B-Minor Mass, Magnificat, St. John Passion, St. Matthew Passion &amp; Weimar Cantatas hours</li>
        <li class="cont">Guidance in planning individual concert itinerary</li>
        <li>Professional development or continuing education credit</li>
      </ul>
      <p class="para" style="margin-top:9px;padding-left:4px">Daniel Marsh partnered with Meridian Classic Tours &amp; Music Festivals to bring you and experience of a Lifetime. With over 100 years of combined educational student travel expertise, Meridian Classic Tours, powered by Garnet Tours, brings unparalleled tour experiences for you and your students.</p>
    </div>

    <div class="block" style="top:336px">
      <h2 class="heading" style="padding-left:4px">Trip Inclusions</h2>
      <ul class="bullets bullets--trip" style="margin-top:8px">
        <li>Roundtrip Airfare from Houston</li>
        <li>13 Nights Accomodations, 3 Star Hotels with A/C</li>
        <li>Daily Breakfast</li>
        <li>Access to rehearsal sessions</li>
        <li>Private Luxury Coach Transfer Services for airport transfers and day tours to Berlin, Weimar and Dresden &amp;</li>
        <li class="cont">Prague.</li>
        <li>Professional Local Guides for City Tours in: Berlin, Weimar, Dresden &amp; Prague</li>
        <li class="cont">Entrance Fees to: House of Anton Reisig, Emil Brandt, Karl Osten in Weimar, Lutheran Frauenkirche &amp; Alte Meister</li>
        <li class="cont">Gallery in the Zwinger Palace in Dresden, and Cathedral and Golden Lane in Prague</li>
        <li>All Applicable Taxes and Gratuities for Included Services, Guides, and Drivers</li>
        <li>$2 Million in Professional Liability Insurance</li>
        <li>24-hour Travel Support Staff</li>
      </ul>
      <p class="contact" style="margin-top:2px">For more information contact Dr. Marsh at daniel.marsh@rioverde.edu</p>
    </div>

    <div class="block" style="top:576px">
      <h2 class="heading">Daniel Marsh Bio:</h2>
      <p class="para" style="margin-top:5px">Daniel Marsh is Director of Choral Studies at the Rio Verde State University and the conductor of the Verde Symphony Chorale and the Verde Choral Artists, a professional chamber choir. A native Texan, his degrees are from Hollis Park University, Brazos University and the Pacific Coast University. Recent engagements include conducting the Lenning Requiem in Buffalo, NY, serving on the jury for the Corvara International Choral Festival in Corvara, Greece and the International Choir Championship Harmonia in Tusnia, Bosnia and Herzegovina.</p>
    </div>

    <div class="logo-band">
      <div class="partner partner--meridian"><span class="partner__mark"></span>Meridian Classic Tours</div>
      <div class="partner partner--garnet"><span class="partner__mark"></span>Garnet Tours</div>
    </div>
    <div class="logo-band__base"></div>
  </section>

  <section class="panel panel--front" aria-label="Front of flyer">
    <svg class="front-art" width="525" height="742" viewBox="0 0 525 742">
      <polygon points="0,330 0,372 205,480 320,480 525,245 525,170" fill="var(--sand)"/>
      <polygon points="0,0 525,0 525,170 320,468 205,468 0,355" fill="var(--tan)"/>
      <defs>
        <linearGradient id="stone" x1="0" y1="0" x2="1" y2="1">
          <stop offset="0" stop-color="#e2d3bd"/><stop offset="1" stop-color="#a89a86"/>
        </linearGradient>
        <linearGradient id="street" x1="0" y1="0" x2="1" y2="1">
          <stop offset="0" stop-color="#9a9a98"/><stop offset="0.6" stop-color="#b0584a"/><stop offset="1" stop-color="#7d7a76"/>
        </linearGradient>
        <linearGradient id="marble" x1="0" y1="0" x2="0" y2="1">
          <stop offset="0" stop-color="#f2f2f2"/><stop offset="1" stop-color="#c9c9c9"/>
        </linearGradient>
      </defs>
      <polygon role="img" aria-label="Photograph of historic city-centre buildings with a red brick facade" points="32,400 110,440 150,470 150,540 205,560 205,712 32,712" fill="url(#street)"/>
      <polygon role="img" aria-label="Photograph of an ornate sandstone concert hall facade" points="425,294 492,294 492,712 233,712 233,678 320,618 370,400" fill="url(#stone)"/>
      <path role="img" aria-label="Photograph of a white marble bust of the composer" d="M205,470 L205,420 Q212,395 230,388 L230,340 Q235,312 252,312 Q272,312 276,340 L276,388 Q296,396 302,420 L302,470 Z" fill="url(#marble)"/>
    </svg>

    <p class="front-text date">June 12-16, 2019</p>
    <p class="front-text tour">Guided Study Tour</p>
    <p class="front-text fest">KLANGTAGE</p>
    <p class="front-text place">Dornhalm, Germany</p>
    <p class="front-text invite">Join us for a once in a lifetime ....<br>led by Daniel Marsh....</p>

    <div class="quote">
      <p class="quote__title">Quote</p>
      <p class="quote__text">"This is where it all has begun...<br>this is why our guests have tears in<br>their eyes listening to<br>the St. Matthew Passion or the B-Minor Mass"</p>
      <p class="quote__name">Martin Keller,</p>
      <p class="quote__role">Musicologist, Festival Director</p>
    </div>
  </section>

  <p class="side-label side-label--back">Back</p>
  <p class="side-label side-label--front">Front</p>
</div>
</body>
</html>
```